Web Site Design

We need to design the whole web site for our small start up. We sell hospitality and culinary art internships abroad. I did my own design with WIX which is horrible meanwhile I started with my business. You can see it www.brightvoyage-intern.example I will need you to create a new and attractive web site and to leave it working on wix. The internship destinations are United Arab Emirates, Thailand, China, Spain, Brazil and maybe leave a couple of pages for future destinations.You could also get other ideas of other sites that do internships.

Target Market(s)

Students and recent graduates of hospitality and culinary art majors

Industry/Entity Type

Education

Number of Pages Required

5+ page

Requirements
Must have
• Addittional to our program destinations, or to the pages in the current site. The website must contain a page for Universities or Hotels who require our service

```html
<!DOCTYPE html>
<html lang="en">
<head>
<meta charset="utf-8">
<title>Bright Voyage – Hospitality Internship Program</title>
<link rel="stylesheet" href="https://fonts.googleapis.com/css2?family=Merriweather:ital,wght@0,400;0,700;1,400;1,700&display=swap">
<style>
  :root {
    --teal-deep: #236673;
    --teal: #2a8a8f;
    --teal-light: #7fd0d6;
    --teal-strip: #3a9ea3;
    --nav-bg: #f7f7f7;
    --nav-text: #9aa3a6;
    --section-grey: #f1f2f4;
    --ink: #151515;
    --muted: #a2a2a2;
    --white: #ffffff;
    --footer: #121212;
  }
  * { box-sizing: border-box; margin: 0; padding: 0; }
  html, body { width: 939px; height: 1200px; overflow: hidden; }
  body {
    position: relative;
    font-family: "Merriweather", Georgia, serif;
    color: var(--ink);
    background: var(--white);
  }

  /* Hero */
  .hero {
    position: absolute; left: 0; top: 0; width: 939px; height: 496px;
    background: linear-gradient(180deg, #22656f 0%, #2a6f73 45%, #3c7868 75%, #4a7f72 100%);
    box-shadow: 0 6px 14px rgba(0,0,0,.18);
    z-index: 2;
  }
  .hero-people {
    position: absolute; left: 516px; top: 164px; width: 332px; height: 332px;
    background: linear-gradient(120deg, #3d7d6e 0%, #6a9a5a 35%, #b8a04a 60%, #e8c028 100%);
    border-radius: 140px 140px 0 0;
    opacity: .9;
  }
  .brand {
    position: absolute; top: 14px; left: 0; width: 939px;
    display: flex; justify-content: center; align-items: center; gap: 10px;
  }
  .brand-mark {
    width: 34px; height: 34px; border-radius: 50%;
    border: 2px solid var(--white);
  }
  .brand-name { color: var(--white); font-size: 18px; font-weight: 400; }

  .main-nav {
    position: absolute; left: 126px; top: 63px; width: 688px; height: 35px;
    background: var(--nav-bg);
  }
  .main-nav a {
    position: absolute; top: 0; height: 35px; line-height: 35px;
    font-size: 8.5px; color: var(--nav-text); text-decoration: none;
    transform: translateX(-50%); white-space: nowrap;
  }
  .main-nav a.is-active {
    left: 106px; width: 66px; transform: none; text-align: center;
    background: var(--teal); color: var(--white); font-weight: 700;
  }
  .main-nav a.nav-destinations { left: 242px; }
  .main-nav a.nav-universities { left: 350px; }
  .main-nav a.nav-hotels { left: 444px; }
  .main-nav a.nav-contact { left: 542px; }

  .hero-copy { position: absolute; left: 126px; top: 233px; color: var(--white); }
  .hero-kicker { font-size: 10.5px; font-weight: 700; color: var(--teal-light); }
  .hero-title { margin-top: 10px; font-size: 33px; font-weight: 700; line-height: 43px; }
  .hero-tagline { margin-top: 12px; font-size: 12px; font-style: italic; font-weight: 700; }

  /* Intro / contact */
  .intro {
    position: absolute; left: 0; top: 496px; width: 939px; height: 294px;
    background: var(--section-grey);
  }
  .intro-heading {
    position: absolute; top: 49px; left: 0; width: 939px; text-align: center;
    font-size: 16px; font-weight: 700; line-height: 23px;
  }
  .divider { position: absolute; display: flex; align-items: center; }
  .divider .rule { height: 1px; background: var(--ink); }
  .intro .divider { top: 109px; left: 314px; }
  .intro .divider .rule { width: 144px; }
  .intro .divider svg { margin: 0 12px; }

  .contact-form { position: absolute; top: 145px; left: 126px; width: 688px; }
  .contact-form input {
    position: absolute; top: 0; height: 33px; border: none; background: var(--white);
    font-family: "Merriweather", Georgia, serif; font-style: italic; font-size: 7.5px;
    padding-left: 12px; color: var(--ink);
  }
  .contact-form input::placeholder { color: #8a8a8a; }
  .field-name { left: 0; width: 156px; }
  .field-email { left: 160px; width: 155px; }
  .field-subject { left: 319px; width: 155px; }
  .field-message { left: 478px; width: 209px; }
  .send-button {
    position: absolute; top: 49px; left: 310px; width: 66px; height: 35px;
    background: var(--teal); color: var(--white); border: none;
    font-family: "Merriweather", Georgia, serif; font-weight: 700; font-size: 8.5px;
  }

  /* Destinations */
  .destinations { position: absolute; left: 0; top: 790px; width: 939px; height: 376px; }
  .chart-bar { position: absolute; bottom: 0; width: 37px; background: var(--teal); }
  .chart-bar span {
    display: block; height: 14px; line-height: 14px; text-align: center;
    background: var(--teal-strip); color: var(--white); font-size: 8px; font-weight: 700;
    white-space: nowrap; letter-spacing: -0.2px;
  }
  .bar-francia { left: 262px; height: 200px; }
  .bar-australia { left: 304px; height: 246px; }
  .bar-spain { left: 347px; height: 282px; }
  .bar-china { left: 390px; height: 200px; }
  .bar-payment { left: 433px; height: 246px; }
  .student-photo {
    position: absolute; left: 126px; top: 130px; width: 132px; height: 246px;
    background: linear-gradient(180deg, #6b5a4a 0%, #9a9a98 30%, #8fa0b4 70%, #7a3a30 100%);
    border-radius: 60px 60px 8px 8px;
  }
  .destinations-title {
    position: absolute; left: 499px; top: 61px; font-size: 17.5px; font-weight: 400;
  }
  .destinations .divider { top: 87px; left: 501px; }
  .destinations .divider .rule { width: 143px; margin-left: 8px; }

  .destination-list { position: absolute; left: 500px; top: 116px; list-style: none; width: 314px; }
  .destination {
    position: relative; height: 53px; padding-left: 50px;
  }
  .destination-icon {
    position: absolute; left: 0; top: 0; width: 38px; height: 34px;
    background: var(--teal); display: flex; align-items: center; justify-content: center;
  }
  .destination h3 { font-size: 12px; font-weight: 400; line-height: 14px; margin-top: -1px; }
  .destination p { font-size: 7px; line-height: 12px; color: var(--muted); margin-top: 3px; }

  /* Footer */
  .site-footer {
    position: absolute; left: 0; top: 1166px; width: 939px; height: 34px;
    background: var(--footer); color: var(--white);
  }
  .copyright { position: absolute; left: 125px; top: 12px; font-size: 7.5px; }
  .social { position: absolute; right: 131px; top: 10px; display: flex; gap: 13px; list-style: none; }
  .social li { width: 13px; height: 13px; border-radius: 50%; background: var(--white); }
</style>
</head>
<body>

<header class="hero" role="img" aria-label="Photo of a historic college building tinted teal, with three smiling students looking at a laptop">
  <div class="hero-people" role="img" aria-label="Photo of three students sharing a laptop and notebooks"></div>

  <div class="brand">
    <span class="brand-mark"></span>
    <span class="brand-name">Bright Voyage</span>
  </div>

  <nav class="main-nav">
    <a class="is-active" href="#">Welcome</a>
    <a class="nav-destinations" href="#">Destinations</a>
    <a class="nav-universities" href="#">Universities</a>
    <a class="nav-hotels" href="#">Hotels</a>
    <a class="nav-contact" href="#">Contact US</a>
  </nav>

  <div class="hero-copy">
    <p class="hero-kicker">Bright Voyage</p>
    <h1 class="hero-title">Hospitality<br>Internship Program</h1>
    <p class="hero-tagline">/ Culinary - F&amp;B - Front Office - Guest Relations</p>
  </div>
</header>

<section class="intro">
  <h2 class="intro-heading">Hospitality internships are our specialty! Take your paid internship in<br>one of our top international five-star hotels</h2>
  <div class="divider">
    <span class="rule"></span>
    <svg width="12" height="10" viewBox="0 0 12 10" aria-hidden="true"><path d="M3 1h8L9 8H1z" fill="none" stroke="#2a8a8f" stroke-width="1.4"/><path d="M1 8h8" stroke="#2a8a8f" stroke-width="1.4"/></svg>
    <span class="rule"></span>
  </div>
  <form class="contact-form">
    <input class="field-name" type="text" placeholder="Name">
    <input class="field-email" type="email" placeholder="Email">
    <input class="field-subject" type="text" placeholder="Asunto">
    <input class="field-message" type="text" placeholder="Message">
    <button class="send-button" type="button">Send</button>
  </form>
</section>

<section class="destinations">
  <div class="student-photo" role="img" aria-label="Photo of a young man in a grey hoodie sitting on the floor working on a laptop"></div>
  <div class="chart-bar bar-francia"><span>Francia</span></div>
  <div class="chart-bar bar-australia"><span>Australia</span></div>
  <div class="chart-bar bar-spain"><span>Spain</span></div>
  <div class="chart-bar bar-china"><span>China</span></div>
  <div class="chart-bar bar-payment"><span>Payment</span></div>

  <h2 class="destinations-title">Destinations</h2>
  <div class="divider">
    <svg width="12" height="10" viewBox="0 0 12 10" aria-hidden="true"><path d="M3 1h8L9 8H1z" fill="none" stroke="#2a8a8f" stroke-width="1.4"/><path d="M1 8h8" stroke="#2a8a8f" stroke-width="1.4"/></svg>
    <span class="rule"></span>
  </div>

  <ul class="destination-list">
    <li class="destination">
      <span class="destination-icon"><svg width="20" height="16" viewBox="0 0 20 16" aria-hidden="true"><path d="M6 2h12l-4 11H2z" fill="none" stroke="#fff" stroke-width="1.8"/><path d="M2 13h12M4 8h10" stroke="#fff" stroke-width="1.8"/></svg></span>
      <h3>China</h3>
      <p>Chinese tourists are flocking abroad. With higher earning power, more Chinese people are visiting places such as the UK, USA...</p>
    </li>
    <li class="destination">
      <span class="destination-icon"><svg width="20" height="16" viewBox="0 0 20 16" aria-hidden="true"><path d="M6 2h12l-4 11H2z" fill="none" stroke="#fff" stroke-width="1.8"/><path d="M2 13h12M4 8h10" stroke="#fff" stroke-width="1.8"/></svg></span>
      <h3>Spain</h3>
      <p>Every year millions of tourists travel to Spain, the country has been one of the most important tourist</p>
    </li>
    <li class="destination">
      <span class="destination-icon"><svg width="20" height="16" viewBox="0 0 20 16" aria-hidden="true"><path d="M6 2h12l-4 11H2z" fill="none" stroke="#fff" stroke-width="1.8"/><path d="M2 13h12M4 8h10" stroke="#fff" stroke-width="1.8"/></svg></span>
      <h3>Australia</h3>
      <p>Moving to Australia means running towards opportunities: Australia is a new country where the population, the</p>
    </li>
    <li class="destination">
      <span class="destination-icon"><svg width="20" height="16" viewBox="0 0 20 16" aria-hidden="true"><path d="M6 2h12l-4 11H2z" fill="none" stroke="#fff" stroke-width="1.8"/><path d="M2 13h12M4 8h10" stroke="#fff" stroke-width="1.8"/></svg></span>
      <h3>Francia</h3>
      <p>Famous for its wines and cheeses, France is the world's most popular tourist destination receiving 82 million Chinese tourists are flocking</p>
    </li>
  </ul>
</section>

<footer class="site-footer">
  <p class="copyright">© 2018 Bright Voyage</p>
  <ul class="social" aria-label="Social links">
    <li aria-label="Social profile"></li>
    <li aria-label="Social profile"></li>
    <li aria-label="Social profile"></li>
    <li aria-label="News feed"></li>
  </ul>
</footer>

</body>
</html>
```